Brellowin Redesign Website

Looking for a web design who can think out of the box.
Redesign of www.brellowin.com.au.
Design requirements:
- Use of many different Colors based on icon logo
- Use of nature and animal pictures that symbolize evolution, transition, metamorphosis, change, etc.
- Website background color for each page is based on Icon logo
- Website mood: Transition & Change, Water, Natural cycle, Waves, Natural evolution, Circle, Wheel,
- Landing page design with animated grafik based on logo icon
- Define colorful design flow that incorporates the website content (see attached file)
- Website development in Wix, access will be provided after final design

Target Market(s)

Non-for-profits in Health and Social sector, local small businesses

Industry/Entity Type

Community Development, Health, Aged-Care,

Coding

Coded - Design and coding required

Number of Pages Required

5+ page

Font styles to use
Sans Serif
Other font styles liked:
• MavenPro, Futura,

Colors
00AB8E
00BBA5
67D7C9
C6EFE9
E9F9F6
FFC000
F8CF3A
FAE287
FDF2CF
FEFAEE
F0912C
F2A743
F7CA91
FBE8D2
FDF5EE

Requirements
Must have
• Landing page with animated grafik, responsive design, out-of-box design, all pages and functions on current website, animated text and design ellements on all sides,
Nice to have
• use logo icon for landing page; it would be great if icon could be animated for the landing page, e.g. moving circles that coming out ot the head
Should not have
• look like a wix template, center aligments in block desciptions, corporate look

```html
<!DOCTYPE html>
<html lang="en">
<head>
<meta charset="utf-8">
<title>Brellowin – Website Pages</title>
<link href="https://fonts.googleapis.com/css2?family=Lora:wght@400;700&family=Open+Sans:wght@400;600;700&display=swap" rel="stylesheet">
<style>
:root{
  --stage:#ff9a0d;
  --pink:#e5195e;
  --magenta:#e0176f;
  --orange:#f7a823;
  --coral:#ef6a3a;
  --blue:#29abe2;
  --green:#6cc04a;
  --teal:#2aa69b;
  --teal-dark:#1b8478;
  --mustard:#c2a012;
  --ink:#222;
  --muted:#666;
  --beige:#f3f0ea;
  --ice:#e6f7fb;
  --black:#151515;
}
*{box-sizing:border-box;margin:0;padding:0}
html,body{width:1174px;height:1200px;overflow:hidden;background:var(--stage)}
body{font-family:'Open Sans',sans-serif;color:var(--ink)}
.board{position:absolute;left:0;top:0;width:1904px;height:1946px;transform:scale(.6166);transform-origin:0 0}
.page{position:absolute;width:425px;background:#fff;overflow:hidden;box-shadow:0 2px 8px rgba(0,0,0,.2)}
.serif{font-family:'Lora',serif}
.abs{position:absolute}

.hdr{position:relative;height:43px;background:#fff;z-index:3}
.brand-bump{position:absolute;left:40px;top:-6px;width:64px;height:64px;border-radius:50%;background:#fff;display:flex;flex-direction:column;align-items:center;justify-content:center;gap:3px}
.brand-dot{width:18px;height:18px;border-radius:50%;background:var(--blue)}
.brand-name{font-family:'Lora',serif;font-weight:700;font-size:10px;color:var(--ink)}
.nav{position:absolute;right:38px;top:5px;display:flex;align-items:center;gap:4px}
.nav span{width:33px;height:33px;border-radius:50%;color:#fff;font:600 6px 'Open Sans',sans-serif;display:flex;align-items:center;justify-content:center}
.nav .n1{background:var(--pink)}.nav .n2{background:var(--orange)}.nav .n3{background:var(--blue)}.nav .n4{background:var(--green)}
.nav .login{width:auto;color:var(--ink);padding-left:6px;border-left:1px solid #ccc;height:10px;border-radius:0}

.hero{position:relative;height:237px;display:flex;align-items:center;justify-content:center;text-align:center;color:#fff}
.hero-warm{background:radial-gradient(ellipse at 70% 85%,rgba(245,150,60,.85),transparent 55%),radial-gradient(ellipse at 25% 30%,rgba(240,110,140,.6),transparent 50%),linear-gradient(135deg,#6a2bd0,#d8226e 55%,#e84a30)}
.hero-deep{background:radial-gradient(ellipse at 50% 90%,rgba(210,85,50,.8),transparent 60%),linear-gradient(165deg,#4a1170,#7a1a7a 55%,#b83340)}
.hero-night{background:radial-gradient(ellipse at 70% 90%,rgba(120,40,70,.8),transparent 60%),linear-gradient(165deg,#2a0838,#3f0c4a 60%,#4f1540)}
.hero h1{font:700 17px 'Lora',serif;letter-spacing:.5px}
.hero h1.big{font-size:26px}
.quote{font:400 7.4px/16px 'Lora',serif;text-transform:uppercase}

.h2{font:700 14px 'Lora',serif;color:var(--pink);text-align:center}
.rule{width:24px;height:2px;background:var(--orange);margin:6px auto 0}
.p{font-size:4.2px;line-height:9px;color:var(--muted)}
.btn{display:inline-block;border-radius:10px;color:#fff;font:600 5px 'Open Sans',sans-serif;padding:6px 12px;text-transform:uppercase}

.contact{position:relative;height:162px;background:linear-gradient(135deg,#5ba632,#66b03a 50%,#57a02f)}
.contact h3{position:absolute;left:45px;top:34px;font:400 11px 'Lora',serif;color:#fff}
.c-item{position:absolute;left:47px;color:#fff;font-size:4px}
.c-item b{display:block;font:400 6px 'Lora',serif;text-decoration:underline}
.c-phone{top:56px;display:flex;gap:6px;align-items:center}
.c-phone em{font:400 7px 'Lora',serif;font-style:normal;display:block}
.form{position:absolute;left:187px;top:26px;width:191px;display:grid;grid-template-columns:1fr 1fr;gap:4px 10px}
.form label{font-size:3.6px;color:#fff;display:block;margin-bottom:1px}
.form .f{height:11px;border:1px solid rgba(255,255,255,.6);font-size:3.6px;color:#fff;padding:3px}
.form .wide{grid-column:1/3}
.form .msg{height:36px}
.submit{background:#222;color:#fff;font-size:4px;border-radius:7px;padding:4px 10px;display:inline-block;margin-top:4px}

.footer{position:relative;height:80px;background:var(--black);color:#fff}
.f-brand{position:absolute;left:52px;top:12px;display:flex;flex-direction:column;align-items:center;gap:4px}
.f-brand .brand-dot{width:26px;height:26px;background:var(--orange)}
.f-brand .brand-name{color:#fff;font-size:13px}
.f-links{position:absolute;left:198px;top:22px;display:flex;gap:24px;font-size:4px}
.f-social{position:absolute;left:234px;top:36px;display:flex;gap:3px}
.f-social span{width:10px;height:10px;border:1px solid #fff;border-radius:50%}
.f-copy{position:absolute;left:206px;top:62px;font-size:4px}

.ic{width:46px;height:46px;border-radius:50%;display:flex;align-items:center;justify-content:center;box-shadow:0 0 0 2px #fff,0 0 0 3px currentColor}
.ic-label{font-size:3.8px;font-weight:700;text-align:center;line-height:7px;margin-top:9px;color:var(--ink)}
.review{width:110px;height:102px;background:#fff;padding:10px}
.who{width:110px;display:flex;gap:5px;align-items:center;font-size:4px;line-height:6px}
.who i{flex:none;width:14px;height:14px;border-radius:50%}
.who b{color:var(--coral);font-family:'Lora',serif;display:block}
</style>
</head>
<body>
<div class="board">

<!-- HOME -->
<section class="page" style="left:38px;top:33px;height:1482px">
  <header class="hdr">
    <div class="brand-bump"><span class="brand-dot"></span><span class="brand-name">Brellowin</span></div>
    <nav class="nav"><span class="n1">HOME</span><span class="n2">ABOUT</span><span class="n3">SERVICE</span><span class="n4">CONTACT</span><span class="login">LOGIN</span></nav>
  </header>
  <div class="hero hero-warm" role="img" aria-label="Colourful bokeh light background">
    <svg class="abs" style="left:181px;top:98px" width="34" height="34" viewBox="0 0 34 34"><circle cx="17" cy="17" r="16" fill="#333" stroke="#fff" stroke-width="1.5"/><path d="M13 10v14l11-7z" fill="#fff"/></svg>
    <p class="quote abs" style="left:229px;top:88px;text-align:left">"Every season I tried to move the river,<br>today I learn to move with it, and so<br>the river is changing me."<br>- Selim Varo</p>
  </div>
  <div style="position:relative;height:134px">
    <p class="serif abs" style="left:47px;top:36px;font-size:8.6px;line-height:15px">Our Learnings Over<br>the Years<span style="color:var(--pink)">Technology Alone</span><br><b>Won't Help You</b></p>
    <p class="p abs" style="left:193px;top:34px;width:190px">Fortunately or unfortunately, the shiny technology isn't a silver bullet you have been searching for. New technology can get you only so far. The challenge here is transforming the mindsets, behaviours with the new ways of working. Hence, the combination of these two will lead to true organisational transformation. Improved performance is a combination of being effective, efficient, and knowing.</p>
    <span class="btn abs" style="left:193px;top:92px;background:var(--pink)">Read More</span>
  </div>
  <div style="position:relative;height:181px;display:flex">
    <div style="width:212px;background:linear-gradient(90deg,#7a8290,#b9b4a8 50%,#6d8a3d)" role="img" aria-label="Woman standing between barren land and green field"></div>
    <div style="flex:1;background:linear-gradient(160deg,#29abe2,#1f6fc4);color:#fff;padding:30px 20px 0 20px">
      <span style="display:block;width:18px;height:18px;border-radius:50%;background:#fff;margin-bottom:7px"></span>
      <p class="serif" style="font-size:8.4px;font-weight:700">Non-bios System Review</p>
      <p class="serif" style="font-size:6px;line-height:10px;margin-top:6px">Are You Looking into a Client Management System and Don't Know Where to Begin?</p>
      <p class="p" style="color:#e8f4ff;margin-top:6px">Our team does requirement workshops with your key staff members. Based on the requirements, we do a tool based agnostic research which is the best-fit solution for you, minus provider bias. We also provide a tool-based evaluation of best-fit systems; CRM or LMS or other systems, Non-bios.</p>
    </div>
  </div>
  <div style="position:relative;height:228px;background:var(--beige)">
    <div class="abs" style="left:45px;top:20px;width:340px;display:grid;grid-template-columns:repeat(3,1fr);row-gap:14px">
      <div><div class="ic" style="margin:0 auto;background:var(--coral);color:var(--coral)"><svg width="22" height="22"><circle cx="11" cy="8" r="4" fill="none" stroke="#fff"/><path d="M3 20c2-6 14-6 16 0" fill="none" stroke="#fff"/></svg></div><p class="ic-label">Find the best-fit Client<br>Management System for your<br>organisation without bias</p></div>
      <div><div class="ic" style="margin:0 auto;background:var(--green);color:var(--green)"><svg width="22" height="22"><circle cx="11" cy="5" r="3" fill="none" stroke="#fff"/><circle cx="4" cy="17" r="3" fill="none" stroke="#fff"/><circle cx="18" cy="17" r="3" fill="none" stroke="#fff"/><path d="M11 8v4M6 15l5-3 5 3" stroke="#fff" fill="none"/></svg></div><p class="ic-label">Identify change impact and<br>resistance</p></div>
      <div><div class="ic" style="margin:0 auto;background:var(--pink);color:var(--pink)"><svg width="22" height="22"><rect x="3" y="3" width="16" height="5" fill="none" stroke="#fff"/><rect x="3" y="10" width="16" height="5" fill="none" stroke="#fff"/><path d="M11 15v5" stroke="#fff"/></svg></div><p class="ic-label">Automate your workflows</p></div>
      <div><div class="ic" style="margin:0 auto;background:var(--blue);color:var(--blue)"><svg width="22" height="22"><circle cx="6" cy="8" r="2.5" fill="none" stroke="#fff"/><circle cx="11" cy="8" r="2.5" fill="none" stroke="#fff"/><circle cx="16" cy="8" r="2.5" fill="none" stroke="#fff"/><path d="M3 18h16" stroke="#fff"/></svg></div><p class="ic-label">Build change leaders capacity in<br>your organisation</p></div>
      <div><div class="ic" style="margin:0 auto;background:var(--orange);color:var(--orange)"><svg width="22" height="22"><circle cx="8" cy="11" r="5" fill="none" stroke="#fff"/><circle cx="16" cy="9" r="3" fill="none" stroke="#fff"/></svg></div><p class="ic-label">Develop user stories with key staff<br>members</p></div>
      <div><div class="ic" style="margin:0 auto;background:#7a2a8c;color:#7a2a8c"><svg width="22" height="22"><rect x="4" y="4" width="14" height="9" fill="none" stroke="#fff"/><circle cx="7" cy="17" r="2" fill="#fff"/><circle cx="15" cy="17" r="2" fill="#fff"/></svg></div><p class="ic-label">Facilitate buy-in for change by<br>establishing a shared vision</p></div>
    </div>
    <span class="btn abs" style="left:177px;top:194px;background:var(--coral)">Request Meeting</span>
  </div>
  <div style="position:relative;height:204px;background:var(--magenta);color:#fff">
    <div class="abs" style="left:230px;top:0;width:195px;height:204px;background:linear-gradient(135deg,#b8594a,#d2405f 45%,#a9473c)" role="img" aria-label="Many hands forming a heart shape"></div>
    <p class="serif abs" style="left:40px;top:32px;font-size:10.5px;font-weight:700;line-height:18px">We are Committed to<br><span style="color:#f9c64a">Our Local Community Support!</span></p>
    <p class="p abs" style="left:40px;top:74px;width:180px;color:#fde">We are purpose and people-driven. Think of us as a safe pair of hands. We have a community fund that supports local NFP. I also volunteer as a business coach for women with a global sister organisation.</p>
    <p class="p abs" style="left:40px;top:110px;width:180px;color:#fde">We have extensive experience in working with government agencies and funding bodies. We have worked for aboriginal communities and organisations in the northern territory. We are located in the bay and provide also on-premises services to local NFPs in this region. We pride ourselves on our well-connected network of digital transformation and data experts in Australia and around the world, so our clients get the best-suited services and systems.</p>
  </div>
  <div style="position:relative;height:213px;background:var(--beige)">
    <p class="serif abs" style="left:0;right:0;top:20px;text-align:center;font-size:10px;font-weight:700">What do <span style="color:var(--coral);font-weight:400">Our Clients</span> Have to Say?</p>
    <div class="abs" style="left:40px;top:55px;display:flex;gap:8px">
      <div class="review"><p style="color:var(--orange);font-size:5px">❝ ★★★★★</p><p class="p" style="font-style:italic;margin-top:5px">We are thrilled by the enthusiasm and passion of the group. Their team is highly experienced, human-centred and understand the problems organisations go through while transforming. They truly helped us achieve our objectives.</p></div>
      <div class="review" style="border:1px solid var(--coral)"><p style="color:var(--orange);font-size:5px">❝ ★★★★★</p><p class="p" style="font-style:italic;margin-top:5px">A rare breed of professionals who are both passionate and expert in their field. They are true professionals who truly understand the complexities of the change as well as the moving parts of complex projects.</p></div>
      <div class="review"><p style="color:var(--orange);font-size:5px">❝ ★★★★★</p><p class="p" style="font-style:italic;margin-top:5px">Truly the ultimate change management professionals. Their team even challenge your own way of thinking about certain aspects of the business and help you redefine ideas.</p></div>
    </div>
    <div class="abs" style="left:40px;top:165px;display:flex;gap:8px">
      <div class="who"><i style="background:#a88" role="img" aria-label="Client portrait"></i><span><b>Nora T</b>Operations Manager</span></div>
      <div class="who"><i style="background:#866" role="img" aria-label="Client portrait"></i><span><b>J. Castell</b>Senior Manager Health Services</span></div>
      <div class="who"><i style="background:#987" role="img" aria-label="Client portrait"></i><span><b>R. Ilves</b>Care Manager Community Services</span></div>
    </div>
  </div>
  <div class="contact">
    <h3>Get in Touch with Us</h3>
    <div class="c-item c-phone"><svg width="12" height="12"><circle cx="6" cy="6" r="5.5" fill="none" stroke="#fff"/><path d="M4 3l1 2-1 1 2 2 1-1 2 1-1 2C5 10 2 7 2 4z" fill="#fff"/></svg><span>Phone Number<em>+61491570006</em></span></div>
    <div class="c-item" style="top:84px"><b>Address:</b>#145 Lorem Ipsum Dummy 254<br>2554 lorem Ipsum Text</div>
    <div class="c-item" style="top:114px"><b>Email :</b>hello@brellowin.com</div>
    <div class="form">
      <div><label>YOUR NAME</label><div class="f">Ana Ruiz</div></div>
      <div><label>COMPANY</label><div class="f">Brellowin</div></div>
      <div><label>EMAIL</label><div class="f">ana.ruiz@mail.com</div></div>
      <div><label>PHONE</label><div class="f">+1 888 888 8888</div></div>
      <div class="wide"><label>MESSAGE</label><div class="f msg">Hi, do you have a moment to talk abo...</div></div>
      <div><span class="submit">SUBMIT</span></div>
    </div>
  </div>
  <footer class="footer">
    <div class="f-brand"><span class="brand-dot"></span><span class="brand-name">Brellowin</span></div>
    <div class="f-links"><span>HOME</span><span>ABOUT</span><span>SERVICES</span><span>CONTACT</span></div>
    <div class="f-social"><span></span><span></span><span></span><span></span><span></span></div>
    <p class="f-copy">© Copyright 2022 Brellowin.All Rights Reserved.</p>
  </footer>
</section>

<!-- ABOUT -->
<section class="page" style="left:506px;top:33px;height:1880px">
  <header class="hdr">
    <div class="brand-bump"><span class="brand-dot"></span><span class="brand-name">Brellowin</span></div>
    <nav class="nav"><span class="n1">HOME</span><span class="n2">ABOUT</span><span class="n3">SERVICE</span><span class="n4">CONTACT</span><span class="login">LOGIN</span></nav>
  </header>
  <div class="hero hero-deep" role="img" aria-label="Purple and orange bokeh light background"><h1>WE ARE THE CHANGE EXPERTS</h1></div>
  <div style="position:relative;height:93px;background:var(--ice)">
    <p class="h2 abs" style="left:0;right:0;top:20px">Our Mission is to</p>
    <div class="abs" style="left:36px;top:52px;width:355px;display:flex;justify-content:space-between;font-size:4.4px;text-align:center;line-height:9px">
      <span>Train the organisational muscles<br>for change</span><span style="color:var(--pink)">◇</span><span>View of organisational information 360°<br>systems</span><span style="color:var(--pink)">◇</span><span>Be present for the future change</span>
    </div>
  </div>
  <div style="position:relative;height:270px">
    <div class="abs" style="left:24px;top:20px;width:160px;height:160px;border-radius:50%;background:var(--green)"></div>
    <div class="abs" style="left:42px;top:33px;width:140px;height:140px;border-radius:50%;background:radial-gradient(circle at 40% 40%,#c88a3a,#2f7d8a 60%,#1d3c40)" role="img" aria-label="Kingfisher diving from the water"></div>
    <p class="serif abs" style="left:197px;top:45px;font-size:12px;font-weight:700;color:var(--pink)">Who We Are</p>
    <p class="p abs" style="left:197px;top:75px;width:190px">We are purpose and people-driven. Think of us as a safe pair of hands. We are a highly experienced digital transformation and change management consultants and delivery experts, you're sure to get the desired results. We have a wide international expert network. Our team makes the transformation program smooth for you, your employees, and your customers.</p>
    <p class="p abs" style="left:197px;top:127px;width:190px">We have been providing services all across the globe including several countries in Europe, Asia and Australia. We have been working with and in remote communities for years and have rolled-out different digital transformation projects around Australia.</p>
    <p class="serif abs" style="left:39px;top:190px;font-size:6.4px;color:var(--orange)">At Brellowin, we take an adaptive, holistic approach</p>
    <p class="p abs" style="left:39px;top:204px;width:350px">To address the needs of organisational change and digital transformation. Every organisation at some point undergoes a transition or change in order to either remain viable or to develop and scale. Whether it is about onboarding new systems or employees, growing a department, or merger with another company, these changes can have a significant impact on your business. At Brellowin, we provide services all-around organisational change and digital transformation. Change can impact several areas in an organisation.</p>
  </div>
  <div style="position:relative;height:230px">
    <svg class="abs" style="left:0;top:0" width="425" height="230" viewBox="0 0 425 230"><path d="M0 42C110 20 280 -10 425 20V175C300 200 150 240 40 215 10 208 0 195 0 180Z" fill="#a8dcd6"/><path d="M0 38C120 14 290 -6 410 12 418 22 425 30 425 36V165C300 190 150 225 40 205 10 198 0 190 0 175Z" fill="#2aa69b"/></svg>
    <p class="serif abs" style="left:0;right:0;top:50px;text-align:center;color:#fff;font-size:11px;font-weight:700;line-height:16px">Change can impact several areas<br>in an organisation</p>
    <div class="abs p" style="left:43px;top:108px;width:170px;color:#e6fffb">● Business Processes: New processes and adjustments to adapt to the change<br>● Systems and IT infrastructure: Roll-out of new systems and integration of existing systems<br>● Individuals and Staff Members: Learning new skills, developing new capabilities to adapt to the change</div>
    <div class="abs p" style="left:225px;top:108px;width:160px;color:#e6fffb">● Market shares: New technology or competitors that would affect the market<br>● Data governance: New legislation or systems require an adjustment or review of your data governance structure</div>
  </div>
  <div style="position:relative;height:150px">
    <p class="serif abs" style="left:0;right:0;top:18px;text-align:center;color:var(--pink);font-size:12px;font-weight:700;line-height:20px">We have extensive experience<br>in working with NFP</p>
    <p class="p abs" style="left:58px;top:72px;width:310px;text-align:center">We have extensive experience in working with NFP. Our team understands the challenges of NFP when it comes to transitioning to new client management systems. Our extensive care manager, community development and social work experience is the solid reason behind our thorough understanding of organisation.</p>
    <span class="btn abs" style="left:177px;top:110px;background:var(--coral)">Learn More</span>
  </div>
  <div style="position:relative;height:152px;background:linear-gradient(180deg,#5a6d7a,#3c4a40 55%,#1f2426)" role="img" aria-label="Road through a forest at dusk">
    <p class="serif abs" style="left:0;right:0;top:62px;text-align:center;color:#f3b83a;font-size:13px;font-weight:700">Our Work Style</p>
  </div>
  <div style="position:relative;height:168px">
    <div class="abs" style="left:39px;top:25px;display:flex;gap:12px">
      <div style="width:107px;height:128px;background:var(--mustard);color:#fff;text-align:center;padding:12px 8px"><svg width="22" height="16"><path d="M1 8l6-5 4 3 4-3 6 5-6 6-4-3-4 3z" fill="none" stroke="#fff"/></svg><p class="serif" style="font-size:6px;font-weight:700;margin:6px 0">Collaborative</p><p class="p" style="color:#fff">We thrive on collaboration and the results that come out from a combined effort and vision. Our team works together with clients to truly understand the challenges associated with change and offer a solution that is unique to them.</p></div>
      <div style="width:107px;height:128px;background:var(--pink);color:#fff;text-align:center;padding:12px 8px"><svg width="22" height="16"><path d="M4 14L14 2l4 4-10 10z" fill="none" stroke="#fff"/></svg><p class="serif" style="font-size:6px;font-weight:700;margin:6px 0">Co-Design</p><p class="p" style="color:#fff">We don't know your business as you do. So, let's design the solution that works best for you together. We Co-Design by developing detailed use cases (user stories) to understand the needs of the staff.</p></div>
      <div style="width:107px;height:128px;background:var(--teal-dark);color:#fff;text-align:center;padding:12px 8px"><svg width="22" height="16"><rect x="2" y="1" width="18" height="8" fill="none" stroke="#fff"/><circle cx="5" cy="13" r="2" fill="#fff"/><circle cx="11" cy="13" r="2" fill="#fff"/><circle cx="17" cy="13" r="2" fill="#fff"/></svg><p class="serif" style="font-size:6px;font-weight:700;margin:6px 0">Engaging</p><p class="p" style="color:#fff">We are a team of fun, smart, and passionate people that love what we do. Hence, we engage with clients and stakeholders to create a use case, know the requirements, and develop the right strategy for transformation.</p></div>
    </div>
  </div>
  <div style="position:relative;height:295px">
    <p class="serif abs" style="left:39px;top:22px;font-size:12px;font-weight:700;color:var(--pink)">Founding Director</p>
    <div class="abs p" style="left:39px;top:55px;width:168px">
      <p>Dana has MSc. in Business Information Systems and is a Certified Change Management Professional with over 20 years of experience in a variety of digital transformation and organisational change projects in the private and public sectors.</p>
      <p style="margin-top:5px">She lead multiple software development projects and supported organisations with business process management. Years later, she made the choice to leave the big business and work at the busiest, least funded women's shelter in the region, gaining more experience on the ground working for NFPs.</p>
      <p style="margin-top:5px">Since 2014, she has been working as an independent IT consultant and transformational leader with government agencies and NFPs. Her passion for human-centred design &amp; digital transformation through change management has made her a dedicated transformational leader and mentor who is supremely successful at stakeholder engagement and change facilitation. She is also adept at creating effective communication with stakeholders on all levels. Well-organised, systematic, and diplomatic in building consensus and spearheading teams are just a few of the adjectives we can add to her glory.</p>
      <p style="margin-top:5px">Reach out to her if you have any questions about the certification process or the framework she works in or just wants to have a conversation about Change Management.</p>
    </div>
    <div class="abs" style="left:221px;top:3px;width:156px;height:198px;background:linear-gradient(180deg,#8a5a36,#5c3a22)" role="img" aria-label="Portrait of the founding director"></div>
    <div class="abs" style="left:225px;top:198px;width:148px;height:46px;background:var(--teal-dark);outline:1px solid #fff;outline-offset:-4px;color:#fff;text-align:center;padding-top:13px"><p class="serif" style="font-size:7px;font-weight:700">Dana Whitfield</p><p style="font-size:4px;margin-top:3px">Solution Architect &amp; Change Manager</p></div>
  </div>
  <div class="contact">
    <h3>Get in Touch with Us</h3>
    <div class="c-item c-phone"><svg width="12" height="12"><circle cx="6" cy="6" r="5.5" fill="none" stroke="#fff"/><path d="M4 3l1 2-1 1 2 2 1-1 2 1-1 2C5 10 2 7 2 4z" fill="#fff"/></svg><span>Phone Number<em>+61491570006</em></span></div>
    <div class="c-item" style="top:84px"><b>Address:</b>#145 Lorem Ipsum Dummy 254<br>2554 lorem Ipsum Text</div>
    <div class="c-item" style="top:114px"><b>Email :</b>hello@brellowin.com</div>
    <div class="form">
      <div><label>YOUR NAME</label><div class="f">Ana Ruiz</div></div>
      <div><label>COMPANY</label><div class="f">Brellowin</div></div>
      <div><label>EMAIL</label><div class="f">ana.ruiz@mail.com</div></div>
      <div><label>PHONE</label><div class="f">+1 888 888 8888</div></div>
      <div class="wide"><label>MESSAGE</label><div class="f msg">Hi, do you have a moment to talk abo...</div></div>
      <div><span class="submit">SUBMIT</span></div>
    </div>
  </div>
  <footer class="footer">
    <div class="f-brand"><span class="brand-dot"></span><span class="brand-name">Brellowin</span></div>
    <div class="f-links"><span>HOME</span><span>ABOUT</span><span>SERVICES</span><span>CONTACT</span></div>
    <div class="f-social"><span></span><span></span><span></span><span></span><span></span></div>
    <p class="f-copy">© Copyright 2022 Brellowin.All Rights Reserved.</p>
  </footer>
</section>

<!-- SERVICES -->
<section class="page" style="left:974px;top:38px;height:934px">
  <header class="hdr">
    <div class="brand-bump"><span class="brand-dot"></span><span class="brand-name">Brellowin</span></div>
    <nav class="nav"><span class="n1">HOME</span><span class="n2">ABOUT</span><span class="n3">SERVICE</span><span class="n4">CONTACT</span><span class="login">LOGIN</span></nav>
  </header>
  <div class="hero hero-deep" role="img" aria-label="Purple and orange bokeh light background">
    <p class="quote">"The years ahead will belong to the gatherers,<br>people able to bring the right pieces together at<br>the right moment, weigh them with care, and choose<br>their next step with a clear and steady mind"<br><span style="text-transform:none;font-family:'Open Sans',sans-serif;font-size:6.4px">- E.R. Hallan</span></p>
  </div>
  <div style="position:relative;height:257px">
    <p class="h2" style="padding-top:30px">WHAT WE OFFER</p><div class="rule"></div>
    <div class="abs" style="left:40px;top:65px;display:flex;gap:2px">
      <div style="width:114px;height:148px;background:linear-gradient(180deg,#7a9ab0,#3d5a4a 55%,#1f3a4a)" role="img" aria-label="Mountain lake reflection"></div>
      <div style="width:114px;height:148px;background:linear-gradient(180deg,#c98a2a,#d9b23a 45%,#5a7a22)" role="img" aria-label="Yellow wildflower in a meadow"></div>
      <div style="width:114px;height:148px;background:linear-gradient(180deg,#4a6a4a,#b8783a 50%,#2f6d7a)" role="img" aria-label="Kingfisher rising from water"></div>
    </div>
    <div class="abs serif" style="left:40px;top:222px;width:344px;display:flex;justify-content:space-around;font-size:7px">
      <span>EXPERTISE</span><span>INGENUITY</span><span>CREATIVITY</span>
    </div>
  </div>
  <div style="position:relative;height:151px;border-top:1px solid #cfe9f2">
    <p class="h2" style="padding-top:20px">WHAT WE DO</p><div class="rule"></div>
    <div class="abs" style="left:30px;top:62px;width:365px;display:flex;justify-content:space-between;text-align:center;font-size:5px;line-height:9px">
      <div><svg width="22" height="22"><rect x="3" y="2" width="16" height="8" fill="none" stroke="#6cc04a"/><path d="M4 15h14M4 19h14" stroke="#6cc04a"/></svg><p class="serif">CHANGE<br>MANAGEMENT</p><p style="color:var(--pink);text-decoration:underline">Learn More</p></div>
      <div><svg width="22" height="22"><rect x="2" y="4" width="18" height="12" fill="none" stroke="#6cc04a"/><path d="M5 13l4-4 3 3 5-5" stroke="#6cc04a" fill="none"/></svg><p class="serif">&amp; DIGITAL TRANSFORMATION<br>SYSTEM INTEGRATION</p><p style="color:var(--pink);text-decoration:underline">Learn More</p></div>
      <div><svg width="22" height="22"><path d="M2 8l9-5 9 5zM4 9v9M9 9v9M14 9v9M19 9v9M2 20h18" stroke="#6cc04a" fill="none"/></svg><p class="serif">ORGANISATIONAL<br>DEVELOPMENT</p><p style="color:var(--pink);text-decoration:underline">Learn More</p></div>
      <div><svg width="22" height="22"><circle cx="8" cy="8" r="5" fill="none" stroke="#6cc04a"/><circle cx="15" cy="15" r="4" fill="none" stroke="#6cc04a"/></svg><p class="serif">&amp; PROCESS OPTIMISATION<br>DATA GOVERNANCE</p><p style="color:var(--pink);text-decoration:underline">Learn More</p></div>
    </div>
  </div>
  <div class="contact">
    <h3>Get in Touch with Us</h3>
    <div class="c-item c-phone"><svg width="12" height="12"><circle cx="6" cy="6" r="5.5" fill="none" stroke="#fff"/><path d="M4 3l1 2-1 1 2 2 1-1 2 1-1 2C5 10 2 7 2 4z" fill="#fff"/></svg><span>Phone Number<em>+61491570006</em></span></div>
    <div class="c-item" style="top:84px"><b>Address:</b>#145 Lorem Ipsum Dummy 254<br>2554 lorem Ipsum Text</div>
    <div class="c-item" style="top:114px"><b>Email :</b>hello@brellowin.com</div>
    <div class="form">
      <div><label>YOUR NAME</label><div class="f">Ana Ruiz</div></div>
      <div><label>COMPANY</label><div class="f">Brellowin</div></div>
      <div><label>EMAIL</label><div class="f">ana.ruiz@mail.com</div></div>
      <div><label>PHONE</label><div class="f">+1 888 888 8888</div></div>
      <div class="wide"><label>MESSAGE</label><div class="f msg">Hi, do you have a moment to talk abo...</div></div>
      <div><span class="submit">SUBMIT</span></div>
    </div>
  </div>
  <footer class="footer">
    <div class="f-brand"><span class="brand-dot"></span><span class="brand-name">Brellowin</span></div>
    <div class="f-links"><span>HOME</span><span>ABOUT</span><span>SERVICES</span><span>CONTACT</span></div>
    <div class="f-social"><span></span><span></span><span></span><span></span><span></span></div>
    <p class="f-copy">© Copyright 2022 Brellowin.All Rights Reserved.</p>
  </footer>
</section>

<!-- CONTACT -->
<section class="page" style="left:1441px;top:38px;height:525px">
  <header class="hdr">
    <div class="brand-bump"><span class="brand-dot"></span><span class="brand-name">Brellowin</span></div>
    <nav class="nav"><span class="n1">HOME</span><span class="n2">ABOUT</span><span class="n3">SERVICE</span><span class="n4">CONTACT</span><span class="login">LOGIN</span></nav>
  </header>
  <div class="hero hero-night" role="img" aria-label="Dark purple bokeh light background"><h1 class="big">GET IN TOUCH</h1></div>
  <div class="contact">
    <h3>Get in Touch with Us</h3>
    <div class="c-item c-phone"><svg width="12" height="12"><circle cx="6" cy="6" r="5.5" fill="none" stroke="#fff"/><path d="M4 3l1 2-1 1 2 2 1-1 2 1-1 2C5 10 2 7 2 4z" fill="#fff"/></svg><span>Phone Number<em>+61491570006</em></span></div>
    <div class="c-item" style="top:84px"><b>Address:</b>#145 Lorem Ipsum Dummy 254<br>2554 lorem Ipsum Text</div>
    <div class="c-item" style="top:114px"><b>Email :</b>hello@brellowin.com</div>
    <div class="form">
      <div><label>YOUR NAME</label><div class="f">Ana Ruiz</div></div>
      <div><label>COMPANY</label><div class="f">Brellowin</div></div>
      <div><label>EMAIL</label><div class="f">ana.ruiz@mail.com</div></div>
      <div><label>PHONE</label><div class="f">+1 888 888 8888</div></div>
      <div class="wide"><label>MESSAGE</label><div class="f msg">Hi, do you have a moment to talk abo...</div></div>
      <div><span class="submit">SUBMIT</span></div>
    </div>
  </div>
  <footer class="footer">
    <div class="f-brand"><span class="brand-dot"></span><span class="brand-name">Brellowin</span></div>
    <div class="f-links"><span>HOME</span><span>ABOUT</span><span>SERVICES</span><span>CONTACT</span></div>
    <div class="f-social"><span></span><span></span><span></span><span></span><span></span></div>
    <p class="f-copy">© Copyright 2022 Brellowin.All Rights Reserved.</p>
  </footer>
</section>

</div>
</body>
</html>
```